I need a better looking dashboard for my web application

I have a very table heavy web page that I would like to add a design touch to it. I have the logo and primary colors picked out, I just need some help in adding visual appeal the page. I would also like to add a couple of button to the page as shortcuts. Every spot that has a + sign could have a button added. I would also like to add another graph (the data will be in the uploaded files. Please feel free to ask any questions :-)

```html
<!DOCTYPE html>
<html lang="en">
<head>
<meta charset="utf-8">
<title>ShiftCover Dashboard</title>
<link href="https://fonts.googleapis.com/css2?family=Open+Sans:wght@400;500;600;700&display=swap" rel="stylesheet">
<style>
:root{
  --teal:#29b0d3;
  --teal-soft:#e6f6fb;
  --teal-line:#9fd9ea;
  --purple:#6a4fa3;
  --purple-mid:#a383e0;
  --purple-pale:#d3c6f1;
  --green:#2d9b4f;
  --red:#e0242b;
  --ink:#333a44;
  --muted:#8a8f98;
  --line:#e6e8ee;
  --page:#f7f7fb;
  --white:#ffffff;
}
*{box-sizing:border-box;margin:0;padding:0}
html,body{width:1200px;height:780px;overflow:hidden}
body{font-family:"Open Sans",sans-serif;background:var(--page);color:var(--ink);position:relative}
.abs{position:absolute}

/* sidebar */
.sidebar{position:absolute;left:0;top:0;width:219px;height:780px;background:var(--white);border-right:1px solid var(--line)}
.brand{position:absolute;left:40px;top:32px;display:flex;align-items:center;gap:8px;font-size:22px;font-weight:600;color:var(--teal)}
.brand-mark{width:20px;height:20px;border-radius:50%;background:var(--purple)}
.nav-item{position:absolute;left:20px;width:181px;height:31px;display:flex;align-items:center;padding-left:8px;gap:13px;font-size:13px;color:var(--ink)}
.nav-item svg{width:16px;height:16px;flex:none;stroke:var(--teal);fill:none;stroke-width:1.6}
.nav-item.active{background:var(--teal);color:var(--white);font-weight:600;border-radius:3px}
.nav-item.active svg{stroke:var(--white)}
.nav-item.sub{left:34px;width:167px}
.nav-item .chev{position:absolute;right:16px;width:10px;height:10px}

/* header */
.avatar-main{left:255px;top:22px;width:56px;height:56px;border-radius:50%;border:3px solid var(--teal);background:radial-gradient(circle at 50% 40%,#b9dcef,#5aa8c9)}
.welcome{left:332px;top:22px;font-size:14px}
.user-name{left:330px;top:36px;font-size:30px;font-weight:700;color:var(--purple);display:flex;align-items:center;gap:22px}
.user-name svg{width:14px;height:14px;stroke:var(--teal);fill:none;stroke-width:2}
.top-btn{top:42px;height:31px;border:1px solid #cfd3da;border-radius:3px;background:var(--white);font-size:13px;color:var(--muted);display:flex;align-items:center;justify-content:center}
.top-btn.primary{background:var(--teal-soft);border-color:var(--teal-line);color:var(--ink)}

/* summary cards */
.card{top:108px;width:284px;height:132px;background:var(--white);border:1px solid var(--line);border-radius:6px}
.card-title{position:absolute;left:28px;top:16px;font-size:15px;font-weight:600;white-space:nowrap}
.legend-num{position:absolute;top:82px;font-size:14px;display:flex;align-items:center;gap:8px}
.dot{width:8px;height:8px;border-radius:50%;display:inline-block}
.legend-lbl{position:absolute;top:103px;font-size:13px;color:var(--muted);white-space:nowrap}
.bar-label{position:absolute;top:103px;font-size:13px;color:var(--muted);width:60px;text-align:center;white-space:nowrap}

/* tabs */
.tab{top:284px;font-size:14px;color:var(--muted);white-space:nowrap}
.tab.active{color:var(--teal)}
.tab-line{left:275px;top:317px;width:123px;height:3px;background:var(--teal)}

/* table panel */
.panel{position:absolute;left:259px;top:321px;width:906px;height:423px;background:var(--white);border:1px solid var(--line);border-radius:6px}
.panel-title{position:absolute;left:28px;top:22px;font-size:18px;font-weight:500;white-space:nowrap}
.panel-sep{position:absolute;left:201px;top:20px;width:1px;height:28px;background:#c9cdd4}
.add-btn{position:absolute;left:222px;top:17px;width:76px;height:32px;border:1px solid var(--teal-line);background:var(--teal-soft);border-radius:3px;display:flex;align-items:center;justify-content:center;gap:10px;font-size:13px}
.add-btn svg{width:12px;height:12px;stroke:var(--teal);stroke-width:2}
.view-toggle{position:absolute;left:790px;top:17px;width:57px;height:30px;border:1px solid var(--teal-line);border-radius:5px;display:flex;align-items:center;padding:2px}
.view-toggle span{width:25px;height:24px;display:flex;align-items:center;justify-content:center;border-radius:3px}
.view-toggle span.on{background:var(--teal)}
.filter-btn{position:absolute;left:853px;top:17px;width:30px;height:30px;border:1px solid var(--teal-line);border-radius:5px;display:flex;align-items:center;justify-content:center}
.rule{position:absolute;left:0;width:904px;height:1px;background:var(--line)}
.col-head{position:absolute;top:92px;font-size:13px;font-weight:600;display:flex;align-items:center;gap:10px;white-space:nowrap}
.col-head svg{width:10px;height:10px;stroke:var(--teal);fill:none;stroke-width:2}

.row{position:absolute;left:0;width:904px;height:61px}
.row-avatar{position:absolute;left:33px;top:13px;width:35px;height:35px;border-radius:50%}
.staff-name{position:absolute;left:86px;top:14px;font-size:13px;color:var(--teal);white-space:nowrap}
.staff-role{position:absolute;left:86px;top:31px;font-size:12.5px;white-space:nowrap}
.status{position:absolute;left:219px;top:19px;height:23px;border-radius:5px;color:var(--white);font-size:10px;font-weight:700;letter-spacing:.4px;display:flex;align-items:center;justify-content:center}
.status.assigned{background:var(--green);width:66px}
.status.available{background:var(--purple);width:70px}
.cell{position:absolute;top:22px;font-size:13px;white-space:nowrap}
.act{position:absolute;top:16px;width:43px;height:29px;border:1px solid var(--teal-line);background:var(--teal-soft);border-radius:3px;display:flex;align-items:center;justify-content:center}
.act svg{width:15px;height:15px;fill:none;stroke-width:1.6}
</style>
</head>
<body>

<aside class="sidebar">
  <div class="brand"><span class="brand-mark"></span>ShiftCover</div>

  <div class="nav-item active" style="top:110px"><svg viewBox="0 0 16 16"><path d="M2 7l6-5 6 5v7H2z"/><path d="M6 14V9h4v5"/></svg>Dashboard</div>
  <div class="nav-item" style="top:149px"><svg viewBox="0 0 16 16"><rect x="2" y="3" width="12" height="11" rx="1"/><path d="M2 6h12M5 1v3M11 1v3"/></svg>Calendar</div>
  <div class="nav-item" style="top:187px"><svg viewBox="0 0 16 16"><circle cx="8" cy="8" r="6.5"/><path d="M6.5 5.5l3.5 2.5-3.5 2.5z"/></svg>Demo Outbox</div>
  <div class="nav-item" style="top:226px"><svg viewBox="0 0 16 16"><circle cx="8" cy="5" r="3"/><path d="M2 15c0-3 3-5 6-5s6 2 6 5z"/></svg>Location Admin<svg class="chev" viewBox="0 0 10 10"><path d="M3 1l4 4-4 4"/></svg></div>
  <div class="nav-item" style="top:264px"><svg viewBox="0 0 16 16"><circle cx="6" cy="5" r="2.6"/><path d="M1 14c0-3 2-5 5-5s5 2 5 5zM10 2.5a2.5 2.5 0 010 5M12 9c2 .5 3 2.5 3 5"/></svg>Regular Staff<svg class="chev" viewBox="0 0 10 10"><path d="M1 3l4 4 4-4"/></svg></div>
  <div class="nav-item sub" style="top:303px"><svg viewBox="0 0 16 16"><circle cx="6" cy="5" r="2.6"/><path d="M1 14c0-3 2-5 5-5 1.5 0 2.5.4 3.4 1M10 11l2 2 3-4"/></svg>Manage Regular Staff</div>
  <div class="nav-item sub" style="top:342px"><svg viewBox="0 0 16 16"><path d="M13 9v5H2V3h5"/><path d="M12 1.5l2.5 2.5L8 10.5H5.5V8z"/></svg>Leave Requests</div>
  <div class="nav-item" style="top:380px"><svg viewBox="0 0 16 16"><path d="M6 2H2v12h4M7 8h8M12 5l3 3-3 3"/></svg>Logout</div>
</aside>

<!-- header -->
<div class="abs avatar-main" role="img" aria-label="Profile photo of the signed-in user"></div>
<div class="abs welcome">Welcomeback,</div>
<div class="abs user-name">Evan Marlow<svg viewBox="0 0 14 14"><path d="M2 5l5 5 5-5"/></svg></div>

<div class="abs top-btn" style="left:728px;width:120px">Create Vacancy</div>
<div class="abs top-btn primary" style="left:854px;width:121px">Create Absence</div>
<div class="abs top-btn" style="left:982px;width:88px">Approve 3</div>
<div class="abs top-btn primary" style="left:1077px;width:88px">Approve 8</div>

<!-- card: today's summary -->
<section class="abs card" style="left:259px">
  <div class="card-title">Total Todays Summary</div>
  <div class="abs" style="left:27px;top:38px;font-size:32px;line-height:40px">100</div>
  <div class="abs" style="left:103px;top:52px;width:162px;height:10px;border-radius:5px;background:var(--purple)"></div>
  <div class="abs" style="left:103px;top:52px;width:35px;height:10px;border-radius:5px;background:var(--purple-mid)"></div>
  <div class="legend-num" style="left:27px"><span class="dot" style="background:var(--purple-pale)"></span>5</div>
  <div class="legend-num" style="left:108px"><span class="dot" style="background:var(--purple-mid)"></span>75</div>
  <div class="legend-num" style="left:176px"><span class="dot" style="background:var(--purple)"></span>20</div>
  <div class="legend-lbl" style="left:27px">Unfilled</div>
  <div class="legend-lbl" style="left:108px">Filled</div>
  <div class="legend-lbl" style="left:176px">No sub needed</div>
</section>

<!-- card: monthly job summary -->
<section class="abs card" style="left:570px">
  <div class="card-title">Total Job Monthly Summary</div>
  <div class="abs" style="left:25px;top:96px;width:234px;height:1px;background:var(--line)"></div>
  <div class="abs" style="left:30px;top:69px;width:48px;height:27px;background:var(--purple);color:#fff;font-size:14px;display:flex;align-items:center;justify-content:center">30</div>
  <div class="abs" style="left:90px;top:59px;width:48px;height:9px;background:var(--purple-mid)"></div>
  <div class="abs" style="left:90px;top:73px;width:48px;text-align:center;font-size:14px">10</div>
  <div class="abs" style="left:150px;top:51px;width:48px;height:7px;background:var(--purple-pale)"></div>
  <div class="abs" style="left:150px;top:73px;width:48px;text-align:center;font-size:14px">5</div>
  <div class="abs" style="left:209px;top:51px;width:48px;height:45px;background:var(--teal);font-size:30px;display:flex;align-items:center;justify-content:center">45</div>
  <div class="bar-label" style="left:24px">Unfilled</div>
  <div class="bar-label" style="left:84px">Filled Job</div>
  <div class="bar-label" style="left:144px">No sub</div>
  <div class="bar-label" style="left:203px">Total</div>
</section>

<!-- card: monthly filled rate -->
<section class="abs card" style="left:881px">
  <div class="card-title">Monthly Filled Rate</div>
  <div class="abs" style="left:28px;top:45px;font-size:8px;color:var(--muted)">100%</div>
  <div class="abs" style="left:33px;top:76px;font-size:8px;color:var(--muted)">50%</div>
  <div class="abs" style="left:46px;top:107px;font-size:8px;color:var(--muted)">0</div>
  <div class="abs" style="left:58px;top:113px;width:112px;height:1px;background:var(--line)"></div>
  <div class="abs" style="left:70px;top:50px;width:78px;height:16px;background:var(--purple-pale);color:#fff;font-size:8px;display:flex;align-items:center;justify-content:center">27%</div>
  <div class="abs" style="left:70px;top:66px;width:78px;height:20px;background:var(--purple-mid);color:#fff;font-size:8px;display:flex;align-items:center;justify-content:center">33%</div>
  <div class="abs" style="left:70px;top:86px;width:78px;height:27px;background:var(--purple);color:#fff;font-size:8px;display:flex;align-items:center;justify-content:center">40%</div>
  <div class="abs" style="left:189px;top:50px;font-size:13px;color:var(--muted);display:flex;align-items:center;gap:9px"><span class="dot" style="background:var(--purple-pale)"></span>No sub</div>
  <div class="abs" style="left:189px;top:70px;font-size:13px;color:var(--muted);display:flex;align-items:center;gap:9px"><span class="dot" style="background:var(--purple-mid)"></span>Open</div>
  <div class="abs" style="left:189px;top:90px;font-size:13px;color:var(--muted);display:flex;align-items:center;gap:9px"><span class="dot" style="background:var(--purple)"></span>Filled</div>
</section>

<!-- tabs -->
<div class="abs tab active" style="left:276px">Managed Openings</div>
<div class="abs tab" style="left:420px">Regular Staff Leave Req.</div>
<div class="abs tab" style="left:590px">My Leave Req.</div>
<div class="abs tab" style="left:699px">Location Overview</div>
<div class="abs tab" style="left:834px">Pending Profile Images</div>
<div class="abs tab" style="left:996px">Substitute Attendance</div>
<div class="abs tab-line"></div>

<!-- openings table -->
<section class="panel">
  <div class="panel-title">Manage Openings</div>
  <div class="panel-sep"></div>
  <div class="add-btn"><svg viewBox="0 0 12 12"><path d="M6 0v12M0 6h12"/></svg>Add</div>
  <div class="view-toggle">
    <span><svg width="15" height="15" viewBox="0 0 16 16" fill="none" stroke="var(--teal)" stroke-width="1.6"><path d="M8 1.5A6.5 6.5 0 1014.5 8H8z"/><path d="M10 1.5a5 5 0 014.5 4.5H10z"/></svg></span>
    <span class="on"><svg width="14" height="12" viewBox="0 0 14 12" stroke="#fff" stroke-width="1.4"><path d="M1 2h12M1 5h12M1 8h12M1 11h12"/></svg></span>
  </div>
  <div class="filter-btn"><svg width="15" height="15" viewBox="0 0 16 16" fill="none" stroke="var(--teal)" stroke-width="1.6"><path d="M1.5 2h13L9.5 8.5V14l-3-1.5v-4z"/></svg></div>

  <div class="rule" style="top:70px"></div>
  <div class="col-head" style="left:33px">Regular Staff</div>
  <div class="col-head" style="left:219px">Status</div>
  <div class="col-head" style="left:326px">Summary<svg viewBox="0 0 10 10"><path d="M1 3l4 4 4-4"/></svg></div>
  <div class="col-head" style="left:496px">Location</div>
  <div class="col-head" style="left:585px">Time Slots summary</div>
  <div class="rule" style="top:114px"></div>

  <div class="row" style="top:115px">
    <div class="row-avatar" role="img" aria-label="Staff photo" style="background:linear-gradient(135deg,#e9e4df,#8a6a55)"></div>
    <div class="staff-name">Lena Hartley</div><div class="staff-role">Teacher</div>
    <div class="status assigned">ASSIGNED</div>
    <div class="cell" style="left:326px">Immediate need! Library</div>
    <div class="cell" style="left:500px">WDMS</div>
    <div class="cell" style="left:585px">12/30 - 01/01 (2h 30m)</div>
    <div class="act" style="left:736px"><svg viewBox="0 0 16 16" stroke="var(--teal)"><path d="M11 2l3 3-8 8H3v-3zM2 15h12"/></svg></div>
    <div class="act" style="left:787px"><svg viewBox="0 0 16 16" stroke="var(--teal)"><path d="M1 8s2.5-5 7-5 7 5 7 5-2.5 5-7 5-7-5-7-5z"/><circle cx="8" cy="8" r="2"/></svg></div>
    <div class="act" style="left:838px"><svg viewBox="0 0 16 16" stroke="var(--red)"><path d="M2 4h12M6 4V2h4v2M3.5 4l1 10h7l1-10M6.5 7v5M9.5 7v5"/></svg></div>
  </div>
  <div class="rule" style="top:175px"></div>

  <div class="row" style="top:176px">
    <div class="row-avatar" role="img" aria-label="Staff photo" style="background:linear-gradient(135deg,#d9dade,#4a3428)"></div>
    <div class="staff-name">Omar Bastian</div><div class="staff-role">Food Service</div>
    <div class="status available">AVAILABLE</div>
    <div class="cell" style="left:326px">Seeking Sub for Couns</div>
    <div class="cell" style="left:500px">WDMS</div>
    <div class="cell" style="left:585px">12/30 - 01/01 (2h 30m)</div>
    <div class="act" style="left:736px"><svg viewBox="0 0 16 16" stroke="var(--teal)"><path d="M11 2l3 3-8 8H3v-3zM2 15h12"/></svg></div>
    <div class="act" style="left:787px"><svg viewBox="0 0 16 16" stroke="var(--teal)"><path d="M1 8s2.5-5 7-5 7 5 7 5-2.5 5-7 5-7-5-7-5z"/><circle cx="8" cy="8" r="2"/></svg></div>
    <div class="act" style="left:838px"><svg viewBox="0 0 16 16" stroke="var(--red)"><path d="M2 4h12M6 4V2h4v2M3.5 4l1 10h7l1-10M6.5 7v5M9.5 7v5"/></svg></div>
  </div>
  <div class="rule" style="top:236px"></div>

  <div class="row" style="top:237px">
    <div class="row-avatar" role="img" aria-label="Staff photo" style="background:linear-gradient(135deg,#5d7f8a,#c9b6a8)"></div>
    <div class="staff-name">Clara Vendi</div><div class="staff-role">Food Service</div>
    <div class="status available">AVAILABLE</div>
    <div class="cell" style="left:326px">Seeking Sub for IT</div>
    <div class="cell" style="left:500px">FMS</div>
    <div class="cell" style="left:585px">12/30 - 01/01 (2h 30m)</div>
    <div class="act" style="left:736px"><svg viewBox="0 0 16 16" stroke="var(--teal)"><path d="M11 2l3 3-8 8H3v-3zM2 15h12"/></svg></div>
    <div class="act" style="left:787px"><svg viewBox="0 0 16 16" stroke="var(--teal)"><path d="M1 8s2.5-5 7-5 7 5 7 5-2.5 5-7 5-7-5-7-5z"/><circle cx="8" cy="8" r="2"/></svg></div>
    <div class="act" style="left:838px"><svg viewBox="0 0 16 16" stroke="var(--red)"><path d="M2 4h12M6 4V2h4v2M3.5 4l1 10h7l1-10M6.5 7v5M9.5 7v5"/></svg></div>
  </div>
  <div class="rule" style="top:297px"></div>

  <div class="row" style="top:298px">
    <div class="row-avatar" role="img" aria-label="Staff photo" style="background:linear-gradient(135deg,#f2c43a,#6b3a2a)"></div>
    <div class="staff-name">Nina Parrow</div><div class="staff-role">Teacher’s Aide</div>
    <div class="status available">AVAILABLE</div>
    <div class="cell" style="left:326px">Substitute &nbsp;needed for ..</div>
    <div class="cell" style="left:500px">FMS</div>
    <div class="cell" style="left:585px">12/30 - 01/01 (2h 30m)</div>
    <div class="act" style="left:736px"><svg viewBox="0 0 16 16" stroke="var(--teal)"><path d="M11 2l3 3-8 8H3v-3zM2 15h12"/></svg></div>
    <div class="act" style="left:787px"><svg viewBox="0 0 16 16" stroke="var(--teal)"><path d="M1 8s2.5-5 7-5 7 5 7 5-2.5 5-7 5-7-5-7-5z"/><circle cx="8" cy="8" r="2"/></svg></div>
    <div class="act" style="left:838px"><svg viewBox="0 0 16 16" stroke="var(--red)"><path d="M2 4h12M6 4V2h4v2M3.5 4l1 10h7l1-10M6.5 7v5M9.5 7v5"/></svg></div>
  </div>
  <div class="rule" style="top:358px"></div>

  <div class="row" style="top:359px">
    <div class="row-avatar" role="img" aria-label="Staff photo" style="background:linear-gradient(135deg,#e5e1dc,#8a5a3c)"></div>
    <div class="staff-name">Adaeze Kolin</div><div class="staff-role">Teacher</div>
    <div class="status available">AVAILABLE</div>
    <div class="cell" style="left:326px">Seeking Sub for Couns</div>
    <div class="cell" style="left:500px">FMS</div>
    <div class="cell" style="left:585px">12/30 - 01/01 (2h 30m)</div>
    <div class="act" style="left:736px"><svg viewBox="0 0 16 16" stroke="var(--teal)"><path d="M11 2l3 3-8 8H3v-3zM2 15h12"/></svg></div>
    <div class="act" style="left:787px"><svg viewBox="0 0 16 16" stroke="var(--teal)"><path d="M1 8s2.5-5 7-5 7 5 7 5-2.5 5-7 5-7-5-7-5z"/><circle cx="8" cy="8" r="2"/></svg></div>
    <div class="act" style="left:838px"><svg viewBox="0 0 16 16" stroke="var(--red)"><path d="M2 4h12M6 4V2h4v2M3.5 4l1 10h7l1-10M6.5 7v5M9.5 7v5"/></svg></div>
  </div>
</section>

</body>
</html>
```